Updated Business Card Design more modern and eye catching

looking for something more dynamic than the sterile card we have now. Please take a look at our web site www.brightmarkfitout.net to see what we do. only looking for the front side of the card for now. I've also attached a sample of a card with raised spot uv ink - it might be cool to incorporate something like that. Card should be bold yet serious. No frilly or scrolly stuff on it.
Updates
Target Market(s)
We do decor and signage for retail business and supermarkets. Our new name should reflect that we're hip but serious.
Contact Information for Business Card
standard business card size - horizontal preferred
Requirements
Must have
- Current logo and colors cannot be changed.
Nice to have
- Must have information shown on existing card but open to some changes. Okay to consider spot uv.
Should not have
- Not busy with pictures in the background.

```html
<!DOCTYPE html>
<html lang="en">
<head>
<meta charset="utf-8">
<title>Brightmark Fitout – Business Card</title>
<link rel="stylesheet" href="https://fonts.googleapis.com/css2?family=Open+Sans:wght@400;600;700&display=swap">
<style>
  :root {
    --backdrop: #e9e7e3;
    --card-white: #f7f6f4;
    --card-black: #050505;
    --gold: #b5a444;
    --ink: #111111;
    --text-light: #ffffff;
  }
  * { margin: 0; padding: 0; box-sizing: border-box; }
  html, body {
    width: 1200px; height: 900px; overflow: hidden;
    background: var(--backdrop);
    font-family: "Open Sans", Arial, sans-serif;
  }
  .card {
    position: absolute; left: 180px; top: 190px;
    width: 840px; height: 520px;
    background: var(--card-black);
    box-shadow: 0 18px 40px rgba(0,0,0,0.18);
    overflow: hidden;
  }
  .card__top {
    position: absolute; left: 0; top: 0; width: 100%; height: 263px;
    background: linear-gradient(180deg, #ffffff 0%, var(--card-white) 100%);
    border-bottom: 4px solid var(--gold);
  }
  .brand {
    position: absolute; left: 0; right: 0; top: 112px;
    display: flex; align-items: center; justify-content: center; gap: 22px;
  }
  .brand__square {
    width: 54px; height: 54px;
    border: 3px solid var(--gold);
  }
  .brand__name {
    font-weight: 600; font-size: 44px; letter-spacing: 3px;
    color: var(--ink); text-transform: uppercase; line-height: 1;
  }
  .person {
    position: absolute; right: 459px; top: 330px; text-align: right;
  }
  .person__name {
    font-weight: 700; font-size: 30px; letter-spacing: 1px;
    color: var(--gold); line-height: 1.1;
  }
  .person__title {
    font-size: 22px; color: var(--text-light); margin-top: 4px;
  }
  .divider {
    position: absolute; left: 420px; top: 312px; width: 1px; height: 114px;
    background: #8d8d8d;
  }
  .contacts {
    position: absolute; left: 448px; top: 306px; list-style: none;
  }
  .contacts li {
    display: flex; align-items: center; gap: 6px;
    font-size: 23px; line-height: 31px; color: var(--text-light);
  }
  .contacts svg { width: 18px; height: 18px; fill: var(--gold); flex: none; }
  .address {
    position: absolute; left: 137px; top: 452px;
    font-size: 22px; color: var(--text-light);
  }
</style>
</head>
<body>
  <div class="card">
    <div class="card__top">
      <div class="brand">
        <span class="brand__square"></span>
        <span class="brand__name">Brightmark Fitout</span>
      </div>
    </div>

    <div class="person">
      <div class="person__name">DANA WHITFIELD</div>
      <div class="person__title">Vice-President</div>
    </div>

    <div class="divider"></div>

    <ul class="contacts">
      <li>
        <svg viewBox="0 0 20 20" aria-hidden="true"><path d="M2 8c0-3 3-5 8-5s8 2 8 5l-1 2-4-1V7H7v2l-4 1zM5 12h10l1 6H4z"/></svg>
        555.018.2240
      </li>
      <li>
        <svg viewBox="0 0 20 20" aria-hidden="true"><path d="M6 1h8a1 1 0 0 1 1 1v16a1 1 0 0 1-1 1H6a1 1 0 0 1-1-1V2a1 1 0 0 1 1-1zm1 3v11h6V4zm3 12.2a1 1 0 1 0 0 .1z"/></svg>
        555.018.7791 ext.3
      </li>
      <li>
        <svg viewBox="0 0 20 20" aria-hidden="true"><path d="M2 5h16v1l-8 5-8-5zm0 3 8 5 8-5v8H2z"/></svg>
        Dana@BrightmarkFitout.net
      </li>
      <li>
        <svg viewBox="0 0 20 20" aria-hidden="true"><circle cx="10" cy="10" r="8"/></svg>
        www.brightmarkfitout.net
      </li>
    </ul>

    <p class="address">1420 Commerce Way Harbor City, FL 34000</p>
  </div>
</body>
</html>
```